Business Card Re-design

We are looking for a fresh bold look for general office business cards. We are a staffing agency that staffs industrial, coal mining, and clerical jobs.
Tag Line: We connect the RIGHT people with the RIGHT jobs.
Evansville Office: 437 W. Hollowmere Ave, Evansville, IN - 47298
p. 812.555.0183 f. 812.555.0196
Princeton Office: 926 S. Larkfen Way, Princeton, IN - 47231
p. 812.555.0127 f. 812.555.0196
Absentee/Emergency 24hr Hotline 812.555.0164 opt.1
www.tallowcrestworkforce.example

```html
<!DOCTYPE html>
<html lang="en">
<head>
<meta charset="utf-8">
<title>Tallowcrest Workforce – Business Cards</title>
<link rel="stylesheet" href="https://fonts.googleapis.com/css2?family=Roboto:wght@400;500;700&display=swap">
<style>
  :root {
    --backdrop: #1f1f20;
    --card-white: #f3f3f2;
    --navy: #003a63;
    --green: #3f9b45;
    --text-grey: #5a5a5a;
    --white: #ffffff;
  }
  * { margin: 0; padding: 0; box-sizing: border-box; }
  html, body {
    width: 1200px; height: 960px; overflow: hidden;
    background: var(--backdrop);
    font-family: "Roboto", Arial, sans-serif;
  }
  .canvas { position: relative; width: 1200px; height: 960px; }

  .card { position: absolute; width: 600px; height: 343px; }
  .card-front { left: 314px; top: 113px; background: var(--card-white); }
  .card-back { left: 311px; top: 472px; background: var(--navy); color: var(--white); text-align: center; }

  .brand-name {
    position: absolute; left: 0; right: 0; top: 168px;
    text-align: center; color: var(--navy);
    font-weight: 700; font-size: 34px; line-height: 42px; letter-spacing: 1px;
    text-transform: uppercase;
  }
  .card-front .brand-name { top: 58px; }
  .brand-name span { display: block; }

  .front-contact {
    position: absolute; left: 0; right: 0; top: 180px;
    text-align: center; color: var(--text-grey);
  }
  .website { font-size: 15px; font-weight: 500; line-height: 20px; }
  .hotline-label { font-size: 16px; line-height: 21px; }
  .hotline-number { font-size: 17px; font-weight: 700; line-height: 21px; }

  .social-row {
    position: absolute; top: 255px; left: 0; right: 0;
    display: flex; justify-content: center; gap: 3px;
  }
  .social-dot { width: 26px; height: 26px; border-radius: 50%; background: var(--navy); }

  .tagline-band {
    position: absolute; left: 0; right: 0; top: 296px; height: 35px;
    background: var(--navy);
    border-top: 2px solid var(--green); border-bottom: 2px solid var(--green);
    box-shadow: inset 0 1px 0 var(--white), inset 0 -1px 0 var(--white);
    color: var(--white); font-size: 15px; font-weight: 500;
    display: flex; align-items: center; justify-content: center;
  }

  .card-back .brand-name { top: 72px; color: var(--white); font-size: 24px; line-height: 28px; }

  .offices { position: absolute; left: 0; right: 0; top: 170px; font-size: 14px; line-height: 19.5px; }
  .office + .office { margin-top: 9px; }
  .office-title { font-weight: 500; }
  .office b { font-weight: 700; }
</style>
</head>
<body>
<main class="canvas">
  <section class="card card-front" aria-label="Business card front">
    <h1 class="brand-name"><span>Tallowcrest</span><span>Workforce</span></h1>
    <div class="front-contact">
      <p class="website">tallowcrestworkforce.example</p>
      <p class="hotline-label">Absentee/Emergency 24hr Hotline</p>
      <p class="hotline-number">812.555.0164 opt.1</p>
    </div>
    <div class="social-row" role="img" aria-label="Social media links">
      <span class="social-dot"></span>
      <span class="social-dot"></span>
      <span class="social-dot"></span>
      <span class="social-dot"></span>
    </div>
    <p class="tagline-band">We connect the RIGHT people with the RIGHT jobs.</p>
  </section>

  <section class="card card-back" aria-label="Business card back">
    <p class="brand-name">Tallowcrest Workforce</p>
    <div class="offices">
      <div class="office">
        <p class="office-title">EVANSVILLE OFFICE</p>
        <p>437 W. Hollowmere Ave, Evansville, IN - 47298</p>
        <p><b>P</b>. 812.555.0183 <b>F</b>. 812.555.0196</p>
      </div>
      <div class="office">
        <p class="office-title">PRINCETON OFFICE:</p>
        <p>926 S. Larkfen Way, Princeton, IN - 47231</p>
        <p><b>P</b>. 812.555.0127&nbsp; <b>F</b>. 812.555.0196</p>
      </div>
    </div>
  </section>
</main>
</body>
</html>
```